Varga Lillas Physiotherapy Business Card Vienna

We need a business card design for a newly created Physiotherapy company based in Vienna Austria.
We seek a simple, modern, minimalist design without too much color variation. The font should look young/fresh, but definitely not childish or so. Since we are a starting Business, we currently haven't got a logo, if you feel like a logo would fit your design, feel free to use one, but it's not necessary.
Target Market(s)
Healthcare, young and elderly people with mobility issues
Industry/Entity Type
Health And Wellness
Contact Information for Business Card
Name: Lilla Varga
Title description: Physiotherapist
Phone num: +43 664 5290 4816
e-mail: lilla.praxis@brelomail.com
Colors
Designer to choose colors to be used in the design.
Requirements
Must have
- Final design language must be in German, basically, the Title Description needs to be "Physiotherapeutin" the other details remain as in the English Language.
Nice to have
- Simple, modern, minimalist design
Should not have
- too many colors, Obvious use of a skeleton, skull, spline

```html
<!DOCTYPE html>
<html lang="de">
<head>
<meta charset="utf-8">
<title>Varga Lillas Physiotherapy – Visitenkarte</title>
<link rel="stylesheet" href="https://fonts.googleapis.com/css2?family=Montserrat:wght@300;400;700&display=swap">
<style>
  :root {
    --backdrop: #d2d2d2;
    --card-front: #ffffff;
    --card-back: #eb9322;
    --ink: #1e1e1e;
    --on-accent: #ffffff;
  }
  * { margin: 0; padding: 0; box-sizing: border-box; }
  html, body {
    width: 900px;
    height: 1200px;
    overflow: hidden;
    background: var(--backdrop);
    font-family: "Montserrat", Arial, sans-serif;
  }
  .canvas {
    position: relative;
    width: 900px;
    height: 1200px;
  }
  .card {
    position: absolute;
    left: 126px;
    width: 647px;
    height: 378px;
  }
  .card--front {
    top: 158px;
    background: var(--card-front);
    color: var(--ink);
    text-align: center;
  }
  .card--back {
    top: 610px;
    background: var(--card-back);
    color: var(--on-accent);
  }
  .contact {
    position: absolute;
    left: 0;
    right: 0;
    top: 124px;
  }
  .contact__name {
    font-weight: 400;
    font-size: 28px;
    letter-spacing: 5px;
    line-height: 34px;
    padding-left: 5px;
  }
  .contact__title {
    font-weight: 400;
    font-size: 13.5px;
    letter-spacing: 3px;
    line-height: 18px;
    padding-left: 3px;
    margin-top: 2px;
  }
  .contact__divider {
    display: block;
    width: 14px;
    height: 1.5px;
    background: var(--ink);
    margin: 10px auto 12px;
  }
  .contact__line {
    font-weight: 400;
    font-size: 14.5px;
    letter-spacing: 2px;
    line-height: 22px;
    padding-left: 2px;
  }
  .contact__line--email { letter-spacing: 1.4px; }
  .brand {
    position: absolute;
    right: 40px;
    bottom: 34px;
    text-align: right;
  }
  .brand__name {
    font-weight: 700;
    font-size: 31px;
    letter-spacing: 5px;
    line-height: 34px;
    margin-right: -5px;
  }
  .brand__field {
    font-weight: 300;
    font-size: 15px;
    letter-spacing: 10.5px;
    line-height: 20px;
    margin-right: -10.5px;
    margin-top: 2px;
  }
</style>
</head>
<body>
  <main class="canvas">
    <section class="card card--front" aria-label="Visitenkarte Vorderseite">
      <div class="contact">
        <h1 class="contact__name">LILLA VARGA</h1>
        <p class="contact__title">PHYSIOTHERAPEUTIN</p>
        <span class="contact__divider" aria-hidden="true"></span>
        <p class="contact__line">+43 664 5290 4816</p>
        <p class="contact__line contact__line--email">lilla.praxis@brelomail.com</p>
      </div>
    </section>
    <section class="card card--back" aria-label="Visitenkarte Rückseite">
      <div class="brand">
        <p class="brand__name">VARGA LILLAS</p>
        <p class="brand__field">PHYSIOTHERAPY</p>
      </div>
    </section>
  </main>
</body>
</html>
```